Investment Funding, Building and Construction

I need a design logo for my new business based out of Houston, TX called Kestrel Ridge Holdings LLC., We are a company looking to help fund and invest into other small/businesses that do not want to deal with the banking system. We also remodel, renovate, and build from the ground up anything from residential, industrial warehousing, and commercial buildings. We would like the design to express our great deal of passion that we have for the work, our dedication to helping the costumer/businesses receive their expectation of work and also our professionalism and commitment to making sure we get the job done as perfect as possible. We want to build your future!

Target Market(s)

Architects, Design Companies, Home Owners and Real Estate

Industry/Entity Type

Construction Company

Contact Information for Business Card

Name: Dorian Pellham
Position: CEO/President
Company Name: Kestrel Ridge Holdings LLC.,
Website: www.kestrelridgehold.example
Phone: 281-507-3619
Email: kestrelridgehold@mailbox.example, crewfundflow@mailbox.example

Font styles to use
Serif

Colors
f04a50
3377b5

Requirements
Must have
• Motivational, Inspiring, and Detailed oriented work but simple.
Nice to have
• I would like to see excitement and enthusiasm within the card.
Should not have
• The project can not be boring and lack of detail.

```html
<!DOCTYPE html>
<html lang="en">
<head>
<meta charset="utf-8">
<title>Kestrel Ridge Holdings LLC. — Business Card</title>
<link href="https://fonts.googleapis.com/css2?family=Cinzel:wght@400&family=Montserrat:wght@400;500&family=Source+Sans+3:wght@400&display=swap" rel="stylesheet">
<style>
  :root {
    --backdrop: #d9d9d9;
    --card: #1c1c1d;
    --red: #f04a50;
    --blue: #3377b5;
    --white: #ffffff;
    --text: #f2f2f2;
  }
  * { margin: 0; padding: 0; box-sizing: border-box; }
  html, body {
    width: 1200px; height: 1176px; overflow: hidden;
    background: var(--backdrop);
  }
  .canvas { position: relative; width: 1200px; height: 1176px; }
  .card {
    position: absolute; left: 200px; width: 780px; height: 445px;
    background: var(--card); border-radius: 24px; overflow: hidden;
  }
  .card--front { top: 113px; }
  .card--back { top: 597px; }

  .person { position: absolute; left: 40px; top: 38px; }
  .person__name {
    font-family: "Cinzel", serif; font-size: 27px; color: var(--white);
    letter-spacing: 0.5px; line-height: 1;
  }
  .person__role {
    margin-top: 14px; font-family: "Source Sans 3", sans-serif;
    font-size: 19px; color: var(--red); line-height: 1;
  }
  .person__rule {
    margin-top: 15px; width: 59px; height: 3px; background: var(--blue);
  }

  .brand {
    font-family: "Montserrat", sans-serif; font-weight: 400;
    color: var(--white); text-transform: uppercase; text-align: center;
  }
  .brand--front {
    position: absolute; right: 34px; top: 62px; width: 300px;
    font-size: 19px; letter-spacing: 4px; line-height: 1.5;
  }
  .brand--back {
    position: absolute; left: 0; right: 0; top: 170px;
    font-size: 34px; letter-spacing: 6px; line-height: 1.4;
  }

  .contacts { position: absolute; left: 40px; top: 284px; list-style: none; }
  .contacts__item {
    display: flex; align-items: center; height: 36px;
    font-family: "Source Sans 3", sans-serif; font-size: 19px; color: var(--text);
  }
  .contacts__icon { width: 26px; height: 20px; margin-right: 12px; flex: none; }

  .footer {
    position: absolute; left: 0; right: 0; top: 365px;
    display: flex; align-items: center;
  }
  .footer__rule { flex: 1; height: 3px; }
  .footer__rule--red { background: var(--red); }
  .footer__rule--blue { background: var(--blue); }
  .footer__url {
    padding: 0 18px; font-family: "Montserrat", sans-serif; font-size: 17px;
    letter-spacing: 2px; color: var(--white);
  }
</style>
</head>
<body>
<main class="canvas">
  <section class="card card--front">
    <div class="person">
      <h1 class="person__name">Dorian Pellham</h1>
      <p class="person__role">CEO/President</p>
      <div class="person__rule"></div>
    </div>

    <p class="brand brand--front">Kestrel Ridge Holdings LLC.</p>

    <ul class="contacts">
      <li class="contacts__item">
        <svg class="contacts__icon" viewBox="0 0 26 20" aria-hidden="true">
          <path d="M1 6 Q13 -1 25 6 L22 9 L18 7 L18 5 Q13 3 8 5 L8 7 L4 9 Z" fill="#f04a50"/>
          <rect x="5" y="9" width="16" height="10" rx="2" fill="#f04a50"/>
          <circle cx="13" cy="14" r="3" fill="#1c1c1d"/>
        </svg>281-507-3619</li>
      <li class="contacts__item">
        <svg class="contacts__icon" viewBox="0 0 26 20" aria-hidden="true">
          <g fill="none" stroke="#7a7a7a" stroke-width="1.4">
            <circle cx="13" cy="10" r="9"/>
            <ellipse cx="13" cy="10" rx="4" ry="9"/>
            <line x1="4" y1="10" x2="22" y2="10"/>
            <line x1="5.5" y1="5.5" x2="20.5" y2="5.5"/>
            <line x1="5.5" y1="14.5" x2="20.5" y2="14.5"/>
          </g>
        </svg>www.kestrelridgehold.example</li>
      <li class="contacts__item">
        <svg class="contacts__icon" viewBox="0 0 26 20" aria-hidden="true">
          <rect x="1" y="3" width="24" height="15" fill="#f04a50"/>
          <path d="M1 3 L13 12 L25 3 M1 18 L10 10 M25 18 L16 10" fill="none" stroke="#1c1c1d" stroke-width="1.4"/>
        </svg>kestrelridgehold@mailbox.example</li>
      <li class="contacts__item">
        <svg class="contacts__icon" viewBox="0 0 26 20" aria-hidden="true">
          <rect x="1" y="3" width="24" height="15" fill="#f04a50"/>
          <path d="M1 3 L13 12 L25 3 M1 18 L10 10 M25 18 L16 10" fill="none" stroke="#1c1c1d" stroke-width="1.4"/>
        </svg>crewfundflow@mailbox.example</li>
    </ul>
  </section>

  <section class="card card--back">
    <p class="brand brand--back">Kestrel Ridge<br>Holdings LLC.</p>
    <div class="footer">
      <span class="footer__rule footer__rule--red"></span>
      <span class="footer__url">www.kestrelridgehold.example</span>
      <span class="footer__rule footer__rule--blue"></span>
    </div>
  </section>
</main>
</body>
</html>
```